Updated Business Cards

We need to update our business cards to reflect new services and employees. We are a luxury vacation rental company in Sandpoint, Idaho. Would also like to make the front facing font easier to read (larger fonts) I love the original logo created for our company and want to use this for the back of the business card created like before - with the dark blue color. See previous files.

Front of the card needs to include:
Employee Name
Title
Phone: 555-555-0147 (ext X)
Address: 417 W. Maple St, Ste 6
Fernhollow, ST 83799
Book Direct: www.RestLakeview.example

```html
<!DOCTYPE html>
<html lang="en">
<head>
<meta charset="utf-8">
<title>Harlow Lodging Business Cards</title>
<link href="https://fonts.googleapis.com/css2?family=Montserrat:wght@400;600;700&display=swap" rel="stylesheet">
<style>
  :root {
    --backdrop: #cfd4d4;
    --card: #f1f1ef;
    --navy: #1f2a6b;
    --ink: #3a3a3a;
    --edge: #1b2560;
  }
  * { box-sizing: border-box; margin: 0; padding: 0; }
  html, body { width: 1200px; height: 881px; overflow: hidden; }
  body {
    background: var(--backdrop);
    font-family: "Montserrat", sans-serif;
    position: relative;
  }
  .card {
    position: absolute;
    width: 520px;
    height: 297px;
    background: var(--card);
    border-bottom: 4px solid var(--edge);
    box-shadow: 0 12px 28px rgba(0,0,0,0.18);
  }
  .card-front { left: 50px; top: 292px; }
  .card-back { left: 630px; top: 292px; }

  .brand {
    display: flex;
    align-items: center;
    justify-content: center;
    gap: 10px;
    color: var(--navy);
    font-weight: 700;
    letter-spacing: 0.04em;
    text-transform: uppercase;
    white-space: nowrap;
  }
  .brand-mark { background: var(--navy); flex: none; }
  .card-front .brand {
    position: absolute;
    top: 38px;
    left: 150px;
    right: 30px;
    font-size: 26px;
  }
  .card-front .brand-mark { width: 16px; height: 16px; }
  .card-back .brand {
    position: absolute;
    inset: 0;
    font-size: 36px;
  }
  .card-back .brand-mark { width: 22px; height: 22px; }

  .employee {
    position: absolute;
    top: 122px;
    left: 30px;
    width: 210px;
    text-align: right;
  }
  .employee-name { color: var(--navy); font-weight: 700; font-size: 22px; }
  .employee-title { color: var(--ink); font-size: 15px; margin-top: 6px; }
  .divider {
    position: absolute;
    left: 258px;
    top: 118px;
    width: 2px;
    height: 76px;
    background: var(--navy);
  }
  .contact {
    position: absolute;
    left: 276px;
    top: 120px;
    list-style: none;
    color: var(--ink);
    font-size: 14px;
    white-space: nowrap;
  }
  .contact li { display: flex; align-items: center; gap: 8px; height: 24px; }
  .contact svg { width: 13px; height: 13px; fill: var(--navy); flex: none; }
  .address {
    position: absolute;
    left: 30px;
    bottom: 32px;
    color: var(--ink);
    font-size: 14px;
    white-space: nowrap;
  }
</style>
</head>
<body>
  <section class="card card-front">
    <div class="brand"><span class="brand-mark"></span>Harlow Lodging</div>
    <div class="employee">
      <div class="employee-name">Employee Name</div>
      <div class="employee-title">Title</div>
    </div>
    <div class="divider"></div>
    <ul class="contact">
      <li>
        <svg viewBox="0 0 16 16"><path d="M3 1h3l1.5 4-2 1.3a9 9 0 0 0 4.2 4.2L11 8.5l4 1.5v3a2 2 0 0 1-2 2A12 12 0 0 1 1 3a2 2 0 0 1 2-2z"/></svg>
        555-555-0147 (ext X)
      </li>
      <li>
        <svg viewBox="0 0 16 16"><path d="M1 3h14v10H1z M2 4l6 5 6-5" fill="none" stroke="#1f2a6b" stroke-width="1.6"/></svg>
        Stay@RestLakeview.example
      </li>
      <li>
        <svg viewBox="0 0 16 16"><circle cx="8" cy="8" r="7" fill="none" stroke="#1f2a6b" stroke-width="1.6"/><path d="M1 8h14M8 1c3 3 3 11 0 14M8 1c-3 3-3 11 0 14" fill="none" stroke="#1f2a6b" stroke-width="1.2"/></svg>
        www.RestLakeview.example
      </li>
    </ul>
    <div class="address">417 W. Maple St, Ste 6 Fernhollow, ST 83799</div>
  </section>

  <section class="card card-back">
    <div class="brand"><span class="brand-mark"></span>Harlow Lodging</div>
  </section>
</body>
</html>
```